New Zealand Marlborough Sauvignon Blanc wine packaging design

We need packaging design for our new wine brand, Dunmore Hale. The wine is a New Zealand Marlborough Sauvignon Blanc. We would like the packaging will portray elegance and style with an understated label. We are looking for a label that portrays the elegance of the French Riviera. The label should be round or pill shaped.
Updates

Industry/Entity Type

Wine

Font styles to use
Serif
Sans Serif

Requirements
Must have
• The words in order of importance: Dunmore Hale, Sauvignon Blanc, Marlborough, New Zealand. It should be fit to the bottle posted in the links
Nice to have
• a pill shape or circular shape
Should not have
• Illustrations of wine bottles, wine glasses, or grapes

```html
<!DOCTYPE html>
<html lang="en">
<head>
<meta charset="utf-8">
<title>Dunmore Hale – Sauvignon Blanc Label</title>
<link rel="stylesheet" href="https://fonts.googleapis.com/css2?family=EB+Garamond:wght@400;500&display=swap">
<style>
  :root {
    --backdrop: #f2f2f2;
    --label-grey: #6a6b6d;
    --ring-line: #e4e4e4;
    --label-text: #ffffff;
    --map-gold: #e6c12f;
    --map-amber: #ecb24a;
    --map-coral: #e89366;
  }
  html, body {
    margin: 0;
    padding: 0;
    width: 1200px;
    height: 1200px;
    overflow: hidden;
    background: var(--backdrop);
  }
  .canvas {
    width: 1200px;
    height: 1200px;
    display: block;
  }
  .label-disc { fill: var(--label-grey); }
  .label-ring { fill: none; stroke: var(--ring-line); stroke-width: 1.6; }
  .brand-name {
    font-family: "EB Garamond", serif;
    font-size: 64px;
    font-weight: 400;
    letter-spacing: 2px;
    fill: var(--label-text);
  }
  .varietal, .region {
    font-family: "EB Garamond", serif;
    font-size: 24px;
    font-weight: 400;
    letter-spacing: 0.5px;
    fill: var(--label-text);
  }
</style>
</head>
<body>
<svg class="canvas" viewBox="0 0 1200 1200" xmlns="http://www.w3.org/2000/svg">
  <defs>
    <linearGradient id="map-tone" x1="0" y1="0" x2="1" y2="0">
      <stop offset="0" stop-color="var(--map-gold)"/>
      <stop offset="0.55" stop-color="var(--map-amber)"/>
      <stop offset="1" stop-color="var(--map-coral)"/>
    </linearGradient>
    <path id="brand-arc" d="M 325.6 792.2 A 335 335 0 0 1 658.2 270.1"/>
  </defs>

  <g class="wine-label">
    <circle class="label-disc" cx="600" cy="600" r="440"/>
    <circle class="label-ring" cx="600" cy="600" r="424"/>

    <rect class="country-map" role="img" aria-label="Map of New Zealand in gold-to-coral metallic tones"
          x="187" y="485" width="836" height="190" rx="95"
          fill="url(#map-tone)"
          transform="rotate(-54.6 605 580)"/>

    <text class="brand-name">
      <textPath href="#brand-arc" startOffset="0">DUNMORE HALE</textPath>
    </text>

    <text class="varietal" x="891" y="857" text-anchor="end">SAUVIGNON BLANC</text>
    <text class="region" x="891" y="886" text-anchor="end">MARLBOROUGH</text>
  </g>
</svg>
</body>
</html>
```